I want a two sided business card for T-shirt company.

Front side.
Logo on the front of the card.
- Rodrigo Villalta
- Shirt designer.
- villaltaprintz1@[login to view URL]
- 916-483-7162
Back side
customizes high quality t shirts
sweaters
jerseys
business cards

```html
<!DOCTYPE html>
<html lang="en">
<head>
<meta charset="utf-8">
<title>Villalta Printz – Business Card</title>
<link rel="stylesheet" href="https://fonts.googleapis.com/css2?family=Open+Sans:wght@400;600;700&family=Noto+Serif:wght@400&display=swap">
<style>
  :root {
    --backdrop: #2f5560;
    --card-white: #ffffff;
    --brand-red: #e0202a;
    --brand-red-dark: #b8141d;
    --ink: #1d1d1d;
    --on-red: #ffffff;
  }
  * { box-sizing: border-box; margin: 0; padding: 0; }
  html, body { width: 1200px; height: 900px; overflow: hidden; }
  body {
    background: var(--backdrop);
    font-family: "Open Sans", Arial, sans-serif;
    display: flex;
    align-items: center;
    justify-content: center;
    gap: 48px;
  }
  .card {
    position: relative;
    width: 540px;
    height: 309px;
    border-radius: 28px;
    background: var(--card-white);
    overflow: hidden;
  }

  /* Front side */
  .front .brand {
    position: absolute;
    left: 42px;
    top: 46px;
    display: flex;
    align-items: center;
    gap: 12px;
  }
  .brand-mark {
    width: 22px;
    height: 22px;
    background: var(--brand-red);
  }
  .brand-name {
    font-family: "Open Sans", Arial, sans-serif;
    font-weight: 600;
    font-size: 34px;
    color: var(--brand-red);
    line-height: 1;
  }
  .front .contact-band {
    position: absolute;
    right: 0;
    bottom: 0;
    width: 330px;
    height: 150px;
  }
  .contact-band svg.band-shape { position: absolute; inset: 0; }
  .contact-details {
    position: absolute;
    left: 128px;
    top: 14px;
    color: var(--on-red);
  }
  .person-name {
    font-size: 17px;
    font-weight: 400;
    line-height: 1.2;
  }
  .person-name strong { font-weight: 700; }
  .person-role {
    font-size: 10px;
    margin-bottom: 8px;
  }
  .contact-list { list-style: none; }
  .contact-list li {
    display: flex;
    align-items: center;
    gap: 6px;
    font-size: 10.5px;
    line-height: 1.9;
  }
  .contact-list svg { width: 11px; height: 11px; flex: none; }

  /* Back side */
  .back {
    background: var(--brand-red);
    padding: 14px;
  }
  .back-inner {
    width: 100%;
    height: 100%;
    border-radius: 18px;
    background: var(--card-white);
    display: flex;
    flex-direction: column;
    align-items: center;
    justify-content: center;
    gap: 18px;
  }
  .back .brand-name { font-size: 40px; }
  .back .brand { display: flex; align-items: center; gap: 14px; }
  .back .brand-mark { width: 26px; height: 26px; }
  .tagline {
    font-family: "Noto Serif", Georgia, serif;
    font-size: 12px;
    color: var(--ink);
    text-align: center;
    line-height: 1.5;
  }
</style>
</head>
<body>

  <section class="card front" aria-label="Card front">
    <div class="brand">
      <span class="brand-mark"></span>
      <span class="brand-name">Villalta Printz</span>
    </div>

    <div class="contact-band">
      <svg class="band-shape" viewBox="0 0 330 150" preserveAspectRatio="none" aria-hidden="true">
        <polygon points="40,0 330,0 330,150 40,150 100,75" fill="var(--brand-red)"/>
        <polygon points="0,0 30,0 90,75 30,150 0,150 60,75" fill="var(--brand-red)"/>
        <polygon points="8,40 78,40 108,75 78,110 8,110 38,75" fill="none"/>
        <polygon points="0,52 70,52 92,75 70,98 0,98 22,75" fill="var(--on-red)" opacity="0.95"/>
        <polygon points="0,62 64,62 77,75 64,88 0,88 13,75" fill="var(--brand-red)"/>
      </svg>
      <div class="contact-details">
        <p class="person-name">Rodrigo <strong>Villalta</strong></p>
        <p class="person-role">Shirt designer</p>
        <ul class="contact-list">
          <li>
            <svg viewBox="0 0 12 12" aria-hidden="true"><path d="M3 1l2 2.5-1.2 1.2a6 6 0 0 0 3.5 3.5L8.5 7 11 9l-1 2C5 11 1 7 1 2z" fill="var(--on-red)"/></svg>
            916-483-7162
          </li>
          <li>
            <svg viewBox="0 0 12 12" aria-hidden="true"><rect x="1" y="2.5" width="10" height="7" fill="var(--on-red)"/><path d="M1 2.5l5 4 5-4" fill="none" stroke="var(--brand-red)" stroke-width="1"/></svg>
            villaltaprintz1@[login to view URL]
          </li>
          <li>
            <svg viewBox="0 0 12 12" aria-hidden="true"><circle cx="6" cy="6" r="4.8" fill="none" stroke="var(--on-red)" stroke-width="1.2"/><path d="M1.2 6h9.6M6 1.2c-2.4 3-2.4 6.6 0 9.6M6 1.2c2.4 3 2.4 6.6 0 9.6" fill="none" stroke="var(--on-red)" stroke-width="0.9"/></svg>
            www.websitename.com
          </li>
          <li>
            <svg viewBox="0 0 12 12" aria-hidden="true"><path d="M6 11.5S2 7 2 4.5a4 4 0 0 1 8 0C10 7 6 11.5 6 11.5z" fill="var(--on-red)"/><circle cx="6" cy="4.5" r="1.4" fill="var(--brand-red)"/></svg>
            Ur Address goes here
          </li>
        </ul>
      </div>
    </div>
  </section>

  <section class="card back" aria-label="Card back">
    <div class="back-inner">
      <div class="brand">
        <span class="brand-mark"></span>
        <span class="brand-name">Villalta Printz</span>
      </div>
      <p class="tagline">customizes high quality t shirts<br>sweaters/jerseys</p>
    </div>
  </section>

</body>
</html>
```